card design for engineering consultancy

engineering drafting and project management company the provides drafting services for.
Electrical, Hydraulic, Mechanical, and Civil services
The company is called Q7R Services and logo is as attached
Information on card should be.
1. Logo
2.website : Q7RServices.example
3. email : info@Q7RServices.example
4. Phone: (+61) 400512836
5. Motto: Design - Document - Develop - Deliver

this card should be basically used for business identification only

Target Market(s)

electricians plumbers air conditioning installers and civil contractors

Industry/Entity Type

engineering, drafting, electrical, plumbing, airconditioning, civil

Contact Information for Business Card

1. Logo 2.website : Q7RServices.example 3. email : info@Q7RServices.example 4. Phone: (+61) 400512836 5. Motto: Design - Document - Develop - Deliver

Font styles to use
Serif

Requirements
Must have
• logo
Nice to have
• something inovative and different that makes it stand out from being just another business card

```html
<!DOCTYPE html>
<html lang="en">
<head>
<meta charset="utf-8">
<title>Q7R Services – Business Card</title>
<link rel="stylesheet" href="https://fonts.googleapis.com/css2?family=Montserrat:wght@400;600;700&display=swap">
<style>
  :root {
    --brand-red: #d32433;
    --ink-grey: #4a4a4a;
    --paper: #ffffff;
    --backdrop: #e9e9ea;
    --rule-grey: #5a5a5a;
  }
  * { box-sizing: border-box; margin: 0; padding: 0; }
  html, body {
    width: 1200px; height: 1024px; overflow: hidden;
    background: var(--backdrop);
    font-family: "Montserrat", Arial, sans-serif;
  }
  .canvas { position: relative; width: 1200px; height: 1024px; }

  .card {
    position: absolute; width: 560px; height: 320px;
    box-shadow: 0 10px 28px rgba(0,0,0,0.25);
    overflow: hidden;
  }

  /* Front */
  .card-front { left: 70px; top: 110px; background: var(--brand-red); color: var(--paper); }
  .card-front .wordmark {
    position: absolute; left: 0; right: 0; top: 112px;
    text-align: center; font-weight: 700; font-size: 44px; letter-spacing: 3px;
  }
  .card-front .rule-top {
    position: absolute; right: 0; top: 140px; width: 60px; height: 1px; background: var(--paper);
  }
  .card-front .website-row {
    position: absolute; left: 0; right: 0; top: 196px;
    display: flex; align-items: center; gap: 14px;
  }
  .card-front .website-row .line { flex: 1; height: 1px; background: var(--paper); }
  .card-front .website { font-size: 14px; letter-spacing: 4px; font-weight: 400; }
  .card-front .rule-bottom {
    position: absolute; left: 0; bottom: 46px; width: 200px; height: 1px; background: var(--paper);
  }

  /* Back */
  .card-back { left: 570px; top: 560px; background: var(--paper); color: var(--ink-grey); }
  .card-back .wordmark {
    position: absolute; left: 0; right: 0; top: 56px;
    text-align: center; font-weight: 700; font-size: 40px; letter-spacing: 3px;
  }
  .card-back .motto {
    position: absolute; left: 0; right: 0; top: 128px;
    display: flex; align-items: center; gap: 14px; padding: 0 0 0 0;
  }
  .card-back .motto .line { flex: 1; height: 1px; background: var(--rule-grey); }
  .card-back .motto-items { display: flex; gap: 16px; font-size: 16px; }
  .card-back .motto-items span::before {
    content: ""; display: inline-block; width: 6px; height: 6px; border-radius: 50%;
    background: var(--brand-red); margin-right: 8px; vertical-align: middle;
  }
  .card-back .motto-second { position: absolute; left: 0; right: 0; top: 162px; text-align: center; font-size: 16px; }
  .card-back .motto-second span::before {
    content: ""; display: inline-block; width: 6px; height: 6px; border-radius: 50%;
    background: var(--brand-red); margin-right: 8px; vertical-align: middle;
  }
  .card-back .rule-above-band {
    position: absolute; left: 0; right: 0; top: 218px; height: 1px; background: var(--rule-grey);
  }
  .card-back .contact-band {
    position: absolute; left: 0; right: 0; top: 228px; height: 44px;
    background: var(--brand-red); color: var(--paper);
    display: flex; align-items: center; justify-content: center; gap: 40px; font-size: 15px;
  }
  .card-back .contact-item { display: flex; align-items: center; gap: 8px; }
  .card-back .contact-item svg { width: 18px; height: 18px; }
</style>
</head>
<body>
<main class="canvas">

  <section class="card card-front" aria-label="Card front">
    <div class="wordmark">Q7R SERVICES</div>
    <div class="rule-top"></div>
    <div class="website-row">
      <span class="line"></span>
      <span class="website">Q7RServices.example</span>
      <span class="line"></span>
    </div>
    <div class="rule-bottom"></div>
  </section>

  <section class="card card-back" aria-label="Card back">
    <div class="wordmark">Q7R SERVICES</div>
    <div class="motto">
      <span class="line"></span>
      <div class="motto-items">
        <span>Design</span><span>Document</span><span>Develop</span>
      </div>
      <span class="line"></span>
    </div>
    <div class="motto-second"><span>Deliver</span></div>
    <div class="rule-above-band"></div>
    <div class="contact-band">
      <div class="contact-item">
        <svg viewBox="0 0 24 24" aria-hidden="true">
          <circle cx="12" cy="12" r="12" fill="#fff"/>
          <path d="M8.2 6.5l1.6-.4 1.3 3-1.1.9a7 7 0 0 0 3.9 3.9l.9-1.1 3 1.3-.4 1.6c-.2.6-.8 1-1.5.9A10 10 0 0 1 7.3 8c-.1-.7.3-1.3.9-1.5z" fill="#d32433"/>
        </svg>
        <span>(+61) 400512836</span>
      </div>
      <div class="contact-item">
        <svg viewBox="0 0 24 24" aria-hidden="true">
          <circle cx="12" cy="12" r="12" fill="#fff"/>
          <rect x="6" y="8" width="12" height="8" fill="none" stroke="#d32433" stroke-width="1.5"/>
          <path d="M6 8l6 5 6-5" fill="none" stroke="#d32433" stroke-width="1.5"/>
        </svg>
        <span>info@Q7RServices.example</span>
      </div>
    </div>
  </section>

</main>
</body>
</html>
```